Brightvale Real Estate

We are looking for help with web design for a new company that is revolutionizing the real estate world on the listing side: by charing per hour for top level professional real estate services. We would like the concept to be simple, clean and easily understood.
Updates

We want this website to actually function, not just a static design.

Industry/Entity Type

Real Estate

```html
<!DOCTYPE html>
<html lang="en">
<head>
<meta charset="utf-8">
<title>Brightvale Real Estate</title>
<link rel="stylesheet" href="https://fonts.googleapis.com/css2?family=Open+Sans:wght@300;400;600;700&family=Ubuntu:wght@300;400&display=swap">
<style>
:root{
  --page:#ececec;
  --white:#ffffff;
  --ink:#5e5e5e;
  --ink-soft:#8a8a8a;
  --navy:#1d2b7a;
  --blue:#29a8e0;
  --dark:#2d2d2d;
  --panel:#1f1f1f;
  --field:#141414;
  --rule:#d3d8de;
  --input:#ececec;
  --input-line:#c8c8c8;
}
*{margin:0;padding:0;box-sizing:border-box}
html,body{width:1117px;height:1200px;overflow:hidden}
body{background:var(--page);font-family:"Open Sans",Arial,sans-serif;color:var(--ink);position:relative}
.abs{position:absolute}
a{color:inherit;text-decoration:none}

/* header */
.header{left:149px;top:0;width:818px;height:128px;background:var(--white)}
.brand{left:0;top:30px;display:flex;align-items:center;gap:10px;font-family:"Ubuntu",sans-serif;font-weight:400;font-size:16px;color:var(--ink);letter-spacing:1px}
.brand-dot{width:14px;height:14px;border-radius:50%;background:var(--ink)}
.call{right:0;top:37px;font-size:10px;color:var(--navy)}
.nav-rule{left:0;top:80px;width:818px;height:1px;background:var(--rule)}
.nav-mark{left:36px;top:78px;width:60px;height:2px;background:var(--blue)}
.nav{left:0;top:94px;width:818px;display:flex;justify-content:space-around;font-size:11px;color:var(--ink-soft);font-weight:300}
.nav-strip{left:149px;top:122px;width:818px;height:6px;background:#dcdcdc}

/* hero */
.hero{left:149px;top:128px;width:818px;height:329px;overflow:hidden}
.hero-photo{left:0;top:0;width:818px;height:329px;background:linear-gradient(180deg,#8fb6de 0%,#c9d8e6 28%,#e6ddd0 52%,#cfc3b2 72%,#9fb79a 86%,#e4e0d8 100%)}
.hero-panel{left:0;top:0}
.finder{left:592px;top:83px;width:176px}
.finder h2{font-family:"Ubuntu",sans-serif;font-weight:300;font-size:17px;color:#e8e8e8;margin-bottom:12px;margin-left:4px}
.select{height:27px;margin-bottom:11px;border-radius:6px;background:var(--field);color:#d9d9d9;font-size:10.5px;line-height:27px;padding-left:12px;position:relative;box-shadow:inset 0 1px 2px #000,0 1px 0 #3a3a3a}
.select::after{content:"";position:absolute;right:12px;top:12px;border:3px solid transparent;border-top-color:#555}
.search{height:28px;border-radius:5px;background:var(--blue);color:#cdeafa;font-size:10.5px;text-align:center;line-height:28px;margin-top:6px}
.arrow{top:274px;width:41px;height:44px;background:#151515;color:#fff;display:flex;align-items:center;justify-content:center}

/* services */
.services{left:131px;top:515px;width:858px;height:238px;background:var(--white)}
.service{top:59px;width:180px}
.service-head{display:flex;align-items:center;gap:18px;height:44px}
.service-icon{width:44px;height:44px;border-radius:50%;background:var(--blue);display:flex;align-items:center;justify-content:center}
.service h3{font-weight:400;font-size:16px;color:var(--blue)}
.service p{margin-top:18px;font-size:11px;line-height:13.5px;font-weight:300;color:var(--ink-soft)}
.service .more{display:block;margin-top:8px;font-size:11px;color:var(--blue);font-weight:300}

/* call to action */
.cta{left:130px;top:755px;width:859px;height:80px;background:var(--dark)}
.cta-title{left:83px;top:33px;font-size:12px;color:#e6e6e6}
.cta-text{left:83px;top:53px;font-size:10px;color:#cfcfcf}
.cta-button{left:648px;top:37px;width:127px;height:26px;background:var(--blue);color:#fff;font-size:10px;text-align:center;line-height:26px}

/* footer */
.footer{left:127px;top:865px;width:862px;height:240px;background:var(--white)}
.col{top:55px;font-size:11px;font-weight:300;color:var(--ink-soft)}
.col li{list-style:none;line-height:20.5px}
.col h4{font-weight:300;font-size:11px;color:var(--ink-soft);margin-bottom:10px}
.post p{font-size:10px;line-height:12.5px;width:180px}
.post p a{color:var(--navy)}
.post .date{font-size:10px;margin:9px 0 15px}
.field{width:147px;height:20px;background:var(--input);border:1px solid var(--input-line);border-radius:2px;font-size:9.5px;line-height:18px;padding-left:10px;margin-bottom:5px;color:#9a9a9a}
.subscribe-btn{width:147px;height:20px;background:var(--blue);color:#fff;font-size:9.5px;line-height:20px;padding-left:9px}
.contact li{display:flex;align-items:center;gap:14px;line-height:23px;font-size:10.5px;white-space:nowrap}
.contact svg{flex:none}

/* bottom bar */
.bottom{left:127px;top:1128px;width:862px;height:72px;background:var(--white)}
.social{left:31px;top:32px;display:flex;gap:3px}
.social span{width:17px;height:17px;border-radius:3px;background:#9aa3ad}
.copyright{right:30px;top:35px;font-family:Arial,sans-serif;font-weight:700;font-size:10px;color:#111}
</style>
</head>
<body>

<header class="abs header">
  <div class="abs brand"><span class="brand-dot"></span>Brightvale Real Estate</div>
  <div class="abs call">Call us: (555) - 014 - 2286</div>
  <div class="abs nav-rule"></div>
  <div class="abs nav-mark"></div>
  <nav class="abs nav">
    <a href="#">Home</a><a href="#">About</a><a href="#">Services</a><a href="#">Commercial</a><a href="#">Residential</a><a href="#">Farm</a><a href="#">Land</a><a href="#">Contact</a>
  </nav>
</header>
<div class="abs nav-strip"></div>

<section class="abs hero">
  <div class="abs hero-photo" role="img" aria-label="Photo of a large cream villa with pool, terrace and blue sky"></div>
  <svg class="abs hero-panel" width="818" height="329" viewBox="0 0 818 329">
    <polygon points="587,0 818,0 818,329 494,329" fill="var(--panel)"/>
  </svg>
  <form class="abs finder">
    <h2>I'M Looking for</h2>
    <div class="select">Home</div>
    <div class="select">Location</div>
    <div class="select">My Budget</div>
    <div class="search">Search</div>
  </form>
</section>
<a class="abs arrow" style="left:128px" href="#" aria-label="Previous">
  <svg width="12" height="14" viewBox="0 0 12 14"><path d="M8 2 3 7l5 5" stroke="#fff" stroke-width="2.4" fill="none"/></svg>
</a>
<a class="abs arrow" style="left:944px" href="#" aria-label="Next">
  <svg width="12" height="14" viewBox="0 0 12 14"><path d="M4 2l5 5-5 5" stroke="#fff" stroke-width="2.4" fill="none"/></svg>
</a>

<section class="abs services">
  <div class="abs service" style="left:27px">
    <div class="service-head"><span class="service-icon"><svg width="16" height="14" viewBox="0 0 16 14"><path d="M8 0 0 7h2v7h4V9h4v5h4V7h2z" fill="#fff"/></svg></span><h3>Residential</h3></div>
    <p>Lorem ipsum dolor sit amet this is a sample text that should be replaced later.</p>
    <a class="more" href="#">&lt;&lt; More</a>
  </div>
  <div class="abs service" style="left:235px">
    <div class="service-head"><span class="service-icon"><svg width="16" height="14" viewBox="0 0 16 14"><rect x="0" y="3" width="16" height="11" rx="2" fill="#fff"/><rect x="5" y="0" width="6" height="4" rx="1" fill="none" stroke="#fff" stroke-width="1.5"/></svg></span><h3>Commercial</h3></div>
    <p>Lorem ipsum dolor sit amet this is a sample text that should be replaced later.</p>
    <a class="more" href="#">&lt;&lt; More</a>
  </div>
  <div class="abs service" style="left:446px">
    <div class="service-head"><span class="service-icon"><svg width="20" height="16" viewBox="0 0 20 16"><path d="M2 8h16M2 11h16M2 14h16" stroke="#fff" stroke-width="1.6"/><path d="M10 6V2l4 2-4 1" fill="#fff"/></svg></span><h3>Farm</h3></div>
    <p>Lorem ipsum dolor sit amet this is a sample text that should be replaced later.</p>
    <a class="more" href="#">&lt;&lt; More</a>
  </div>
  <div class="abs service" style="left:655px">
    <div class="service-head"><span class="service-icon"><svg width="20" height="16" viewBox="0 0 20 16"><circle cx="10" cy="5" r="3.5" fill="#fff"/><path d="M0 16 6 10l4 3 4-4 6 7z" fill="#fff"/></svg></span><h3>Land</h3></div>
    <p>Lorem ipsum dolor sit amet this is a sample text that should be replaced later.</p>
    <a class="more" href="#">&lt;&lt; More</a>
  </div>
</section>

<section class="abs cta">
  <div class="abs cta-title">Lorem Ipsum dolor sit amet this is a sample text</div>
  <div class="abs cta-text">Lorem ipsum dolor sit amet this is a sample text and it should be replaced later</div>
  <a class="abs cta-button" href="#">Call To Action</a>
</section>

<footer class="abs footer">
  <ul class="abs col" style="left:27px"><li>About</li><li>Services</li><li>Residential</li><li>Land</li><li>Commercial</li></ul>
  <ul class="abs col" style="left:135px"><li>Privacy</li><li>Terms</li></ul>
  <div class="abs col post" style="left:237px">
    <h4>Latest Post</h4>
    <p>Lorem ipsdum dolor sit amet this is a sample blog post lorem ipsum dolor sit amet <a href="#">&lt;&lt;more</a></p>
    <div class="date">8/9/2013</div>
    <p>Lorem ipsdum dolor sit amet this is a sample blog post lorem ipsum dolor sit amet <a href="#">&lt;&lt;more</a></p>
    <div class="date">8/9/2013</div>
  </div>
  <form class="abs col" style="left:446px">
    <h4>Subscribe</h4>
    <div class="field">Name</div>
    <div class="field">Email</div>
    <div class="subscribe-btn">Subscribe</div>
  </form>
  <div class="abs col" style="left:678px">
    <h4>Contact</h4>
    <ul class="contact">
      <li><svg width="12" height="11" viewBox="0 0 16 14"><path d="M8 0 0 7h2v7h4V9h4v5h4V7h2z" fill="#555"/></svg>Address, 48 Alder Row</li>
      <li><svg width="12" height="12" viewBox="0 0 12 12"><path d="M2 0h3l1 3-2 1c1 2 2 3 4 4l1-2 3 1v3c0 1-1 2-2 2C5 12 0 7 0 2 0 1 1 0 2 0z" fill="#555"/></svg>(555) - 014 - 2286</li>
      <li><svg width="12" height="10" viewBox="0 0 12 10"><rect x=".6" y=".6" width="10.8" height="8.8" fill="none" stroke="#555" stroke-width="1.2"/><path d="M1 1l5 4 5-4" fill="none" stroke="#555" stroke-width="1.2"/></svg>info@brightvale-mail.com</li>
    </ul>
  </div>
</footer>

<div class="abs bottom">
  <div class="abs social" aria-label="Social links"><span></span><span></span><span></span><span></span><span></span></div>
  <div class="abs copyright">Copyrights 2015 Brightvale Real Estate. All Right Reserved</div>
</div>

</body>
</html>
```